New business card and project proposal template, letterhead

Hello, I'm looking for a new business card and project proposal template to go with my new logo. project Proposals are sent to clients as a pdf document. my updated website is www.brightharborfilms.com. Looking for a look of a hollywood studio. Not a lot of dark colors , Red can be used as am acent, but not as a main. (see logo)

Target Market(s)

Communication departments, marketing managers.

Industry/Entity Type

Videography

Colors
ec1f27

Requirements
Must have
• logo,
• Brightharbor Films Inc.
• #300 - 812 East Kingsway
• Vancouver BC V6K 2M8
• www.brightharborfilms.com
• morwen@brightharborfilms.com
• Direct: 604 291 4073
• vimeo.com/brightharborfilms
• twitter: @brightharbor
Should not have
• clowns

```html
<!DOCTYPE html>
<html lang="en">
<head>
<meta charset="utf-8">
<title>Brightharbor Films – Business Card</title>
<link href="https://fonts.googleapis.com/css2?family=Roboto+Condensed:wght@700&family=Open+Sans:wght@400;600;700&family=Roboto:wght@700&display=swap" rel="stylesheet">
<style>
  :root {
    --stage: #d6d6d6;
    --card-light: #f3f3f3;
    --card-dark: #1b1b1c;
    --ink: #1e1e1e;
    --text-grey: #555555;
    --accent: #7d1322;
    --accent-dot: #a3303c;
    --band: #161616;
    --band-text: #f0f0f0;
    --white: #ffffff;
  }
  * { margin: 0; padding: 0; box-sizing: border-box; }
  html, body { width: 1200px; height: 960px; overflow: hidden; }
  body { background: var(--stage); position: relative; font-family: "Open Sans", Arial, sans-serif; }

  .card { position: absolute; border-radius: 18px; overflow: hidden; }
  .card-front { left: 315px; top: 113px; width: 598px; height: 342px; background: var(--card-light); }
  .card-back { left: 312px; top: 473px; width: 599px; height: 341px; background: var(--card-dark); }

  .wordmark { font-family: "Roboto", Arial, sans-serif; font-weight: 700; white-space: nowrap; }
  .tagline { font-family: "Open Sans", Arial, sans-serif; white-space: nowrap; }

  .brand-front { position: absolute; right: 296px; top: 137px; text-align: right; }
  .brand-front .wordmark { font-size: 24px; line-height: 26px; letter-spacing: 0.3px; color: var(--ink); }
  .brand-front .tagline { font-size: 9.5px; line-height: 12px; color: var(--ink); }

  .divider { position: absolute; left: 327px; top: 65px; height: 184px; border-left: 2px dotted var(--accent-dot); }

  .details { position: absolute; left: 354px; top: 62px; }
  .person-name { font-family: "Roboto Condensed", Arial, sans-serif; font-weight: 700; font-size: 23px; line-height: 26px; color: var(--ink); }
  .person-role { font-family: "Roboto Condensed", Arial, sans-serif; font-weight: 700; font-size: 15px; line-height: 18px; color: var(--accent); }
  .address { margin-top: 7px; font-size: 13px; line-height: 19px; color: var(--text-grey); }
  .address .company { font-weight: 700; }
  .contacts { margin-top: 4px; list-style: none; font-size: 13px; line-height: 19px; color: var(--text-grey); }
  .contacts li { display: flex; align-items: center; }
  .contacts svg { width: 12px; height: 12px; margin-right: 10px; flex: none; }

  .web-band { position: absolute; left: 0; top: 297px; width: 100%; }
  .web-band .dots { border-top: 1.5px dotted var(--accent-dot); }
  .web-band .bar { margin: 2px 0; height: 23px; background: var(--band); color: var(--band-text); font-size: 13px; letter-spacing: 3.2px; text-align: center; line-height: 23px; }

  .brand-back { position: absolute; right: 97px; top: 141px; text-align: right; }
  .brand-back .wordmark { font-size: 37px; line-height: 36px; letter-spacing: 0.5px; color: var(--white); }
  .brand-back .tagline { font-size: 14.5px; line-height: 18px; color: var(--white); }
</style>
</head>
<body>
  <section class="card card-front">
    <div class="brand-front">
      <div class="wordmark">BRIGHTHARBORFILMS</div>
      <div class="tagline">framing light. moving audiences.</div>
    </div>

    <div class="divider"></div>

    <div class="details">
      <div class="person-name">MORWEN ASHBY</div>
      <div class="person-role">FOUNDER</div>
      <div class="address">
        <div class="company">Brightharbor Films Inc.</div>
        <div>#300 - 812 East Kingsway</div>
        <div>Vancouver BC V6K 2M8</div>
      </div>
      <ul class="contacts">
        <li>
          <svg viewBox="0 0 12 12" aria-hidden="true"><path fill="#2a2a2a" d="M2.4 0.6 L4.2 2.8 L3.2 4.2 C3.8 5.6 5.4 7.4 7.8 8.8 L9.2 7.8 L11.4 9.6 L10 11.4 C5.6 11 1 6.4 0.6 2 Z"/></svg>
          <span>604 291 4073</span>
        </li>
        <li>
          <svg viewBox="0 0 12 12" aria-hidden="true"><rect x="0.5" y="2.5" width="11" height="7.5" rx="0.8" fill="#2a2a2a"/><path d="M1 3 L6 6.8 L11 3" stroke="#f3f3f3" stroke-width="1" fill="none"/></svg>
          <span>morwen@brightharborfilms.com</span>
        </li>
        <li>
          <svg viewBox="0 0 12 12" aria-hidden="true"><rect x="0.5" y="0.5" width="11" height="11" rx="2" fill="#2a2a2a"/></svg>
          <span>brightharborfilms</span>
        </li>
        <li>
          <svg viewBox="0 0 12 12" aria-hidden="true"><rect x="0.5" y="0.5" width="11" height="11" rx="2" fill="#2a2a2a"/></svg>
          <span>@brightharbor</span>
        </li>
      </ul>
    </div>

    <div class="web-band">
      <div class="dots"></div>
      <div class="bar">www.brightharborfilms.com</div>
      <div class="dots"></div>
    </div>
  </section>

  <section class="card card-back">
    <div class="brand-back">
      <div class="wordmark">BRIGHTHARBORFILMS</div>
      <div class="tagline">framing light. moving audiences</div>
    </div>
  </section>
</body>
</html>
```